Judicial election website to attract voters

I need a simple one-page web design for a judicial election. I'm going to put up one picture, maybe two. The picture I have needs a little touch-up (whiten teeth for example). I have 3 paragraphs of text. I'd like a "Donate" button that can link to a CoinDrift account. I'd also like a little background design, like the Constitution or something like that. There's a couple other little things but that's the bulk of it.

Target Market(s)

Involved voters and some media

Industry/Entity Type

Legal

Number of Pages Required

1 page

Font styles to use
Sans Serif

Requirements
Must have
• My picture, text, donate button
• Phrase "Remember to vote August 30, 2016!"
Nice to have
• Perhaps a second photo, maybe a short 30 second video of me talking directly to the voters, cool background: Constitution, something judgey.
Should not have
• Not sure ... profanity, I guess.

```html
<!DOCTYPE html>
<html lang="en">
<head>
<meta charset="utf-8">
<title>Marlowe — Judicial Election</title>
<link rel="stylesheet" href="https://fonts.googleapis.com/css2?family=Kumbh+Sans:wght@400;600;700&family=Open+Sans:wght@400;600;700&family=Raleway:wght@600;700&display=swap">
<style>
:root{
  --navy:#272a6e;
  --navy-deep:#16183f;
  --hero-a:#23266c;
  --hero-b:#3b3f9e;
  --red:#d0232f;
  --ink:#1e1e1e;
  --text:#555;
  --grey-panel:#e3e3e3;
  --icon-ring:#5a5fc4;
  --footer:#232323;
  --footer-deep:#161616;
  --footer-text:#8a8a8a;
  --field:#3a3a3a;
  --white:#fff;
}
*{box-sizing:border-box;margin:0;padding:0}
html,body{width:1200px;height:3010px;overflow:hidden}
body{font-family:"Open Sans",Arial,sans-serif;color:var(--text);background:var(--white);position:relative}
.abs{position:absolute}
a{color:inherit;text-decoration:none}

/* top bar */
.topbar{position:absolute;left:0;top:0;width:1200px;height:40px;background:#1f1f1f;color:#ddd;font-size:13px}
.topbar .contact{position:absolute;left:64px;top:11px;display:flex;gap:22px;align-items:center}
.topbar .contact span{display:flex;gap:7px;align-items:center}
.topbar .social{position:absolute;right:64px;top:11px;display:flex;gap:8px}
.topbar .social i{width:18px;height:18px;border-radius:50%;background:#fff;display:block}

/* header */
.header{position:absolute;left:0;top:40px;width:1200px;height:104px;background:#fff}
.logo{position:absolute;left:60px;top:32px;font-family:"Kumbh Sans",sans-serif;font-weight:700;font-size:32px;letter-spacing:7px;color:#111}
.nav{position:absolute;right:222px;top:42px;display:flex;gap:28px;font-size:15px;font-weight:600;color:#222}
.donate{position:absolute;left:1030px;top:34px;width:110px;height:42px;background:var(--red);color:#fff;font-size:16px;display:flex;align-items:center;justify-content:center}

/* hero */
.hero{position:absolute;left:0;top:144px;width:1200px;height:470px;background:radial-gradient(ellipse at 60% 55%,var(--hero-b),var(--hero-a) 75%);overflow:hidden}
.hero-photo{position:absolute;left:0;top:0;width:680px;height:470px;background:
  linear-gradient(120deg,rgba(200,40,50,.85) 0%,rgba(240,235,235,.7) 22%,rgba(200,40,50,.6) 38%,rgba(40,45,120,0) 55%),
  radial-gradient(ellipse at 55% 82%,rgba(240,140,60,.9),rgba(200,220,40,.55) 40%,rgba(40,45,120,0) 70%)}
.reminder{position:absolute;left:210px;top:131px;width:452px;height:66px;background:var(--red);color:#fff;font-family:"Kumbh Sans",sans-serif;font-size:26px;display:flex;align-items:center;justify-content:center}
.reminder b{margin-left:8px}
.hero-copy{position:absolute;left:716px;top:50px;width:364px;text-align:center;color:#fff}
.hero-copy .kicker{font-family:"Kumbh Sans",sans-serif;font-size:16px;font-weight:600;letter-spacing:.3px}
.hero-copy h1{font-family:"Kumbh Sans",sans-serif;font-size:42px;font-weight:700;line-height:1;margin-top:12px}
.hero-copy .motto{font-size:14px;font-weight:600;margin-top:12px}
.subscribe{position:absolute;left:716px;top:177px;width:364px;height:245px;background:var(--navy-deep);text-align:center;color:#fff;font-size:15px;line-height:24px;padding-top:24px}
.subscribe .field{width:316px;height:46px;background:#fff;margin:22px auto 0}
.subscribe .btn{width:164px;height:44px;background:var(--red);margin:22px auto 0;font-size:14px;font-weight:700;display:flex;align-items:center;justify-content:center}

/* section titles */
.sec-title{position:absolute;left:0;width:1200px;text-align:center;font-family:"Kumbh Sans",sans-serif;font-weight:400;font-size:46px;color:#111}
.rule{position:absolute;left:540px;width:120px;height:2px;background:#e46a70}
.lead{position:absolute;left:200px;width:800px;text-align:center;font-size:13.5px;line-height:25px;color:#555}

/* features */
.feature{position:absolute;top:862px;width:334px;height:336px;text-align:center}
.feature.is-active{background:var(--grey-panel)}
.feature .icon{width:108px;height:108px;border-radius:50%;background:var(--navy);border:6px solid var(--icon-ring);margin:14px auto 0;display:flex;align-items:center;justify-content:center}
.feature h3{font-family:"Kumbh Sans",sans-serif;font-weight:400;font-size:21px;color:#111;margin-top:22px}
.feature .line{width:150px;height:1px;background:#e46a70;margin:6px auto 0}
.feature p{font-size:13px;line-height:22px;margin:14px auto 0;width:310px}
.btn-red{display:inline-flex;align-items:center;justify-content:center;background:var(--red);color:#fff;font-size:14px;width:108px;height:42px;margin-top:16px}

/* about */
.about{position:absolute;left:0;top:1296px;width:1200px;height:456px;background:var(--navy);color:#fff}
.about .label{position:absolute;left:64px;top:60px;font-family:"Kumbh Sans",sans-serif;font-weight:700;font-size:27px;line-height:30px}
.about .label span{letter-spacing:6px;font-size:34px}
.portrait{position:absolute;left:60px;top:149px;width:233px;height:263px;background:radial-gradient(ellipse at 50% 40%,#e8c9a8,#b8a58e 55%,#9a8a78)}
.about h2{position:absolute;left:315px;top:54px;width:830px;font-size:21px;font-weight:600;line-height:34px}
.about .bio{position:absolute;left:325px;top:136px;width:820px;font-size:12.5px;line-height:22.5px}
.about .bio p+p{margin-top:22px}
.about .btn-red{position:absolute;left:325px;top:366px;width:151px;margin:0}

/* campaign cards */
.card{position:absolute;top:2005px;width:340px}
.card .photo{height:215px}
.card .meta{display:flex;justify-content:space-between;margin-top:34px;font-size:12.5px;color:var(--red)}
.card .meta span{display:flex;gap:4px;align-items:center}
.card h4{font-size:15px;font-weight:700;color:#111;line-height:24px;margin-top:12px}
.card p{font-size:12.5px;line-height:21px;margin-top:8px;color:#555}
.btn-navy{display:inline-flex;align-items:center;justify-content:center;background:var(--navy);color:#fff;font-size:14px;width:113px;height:44px;margin-top:14px}

/* footer */
.footer{position:absolute;left:0;top:2509px;width:1200px;height:457px;background:var(--footer);color:var(--footer-text)}
.f-col{position:absolute;top:64px}
.f-head{font-family:"Raleway",sans-serif;font-weight:600;font-size:21px;color:#fff;display:flex;align-items:center;height:32px}
.f-head b{display:inline-flex;width:26px;height:32px;background:var(--red);align-items:center;justify-content:center;margin-right:2px;font-weight:600}
.news{margin-top:22px;width:252px}
.news li{list-style:none;padding-bottom:14px;margin-bottom:16px;border-bottom:1px solid #333}
.news li:last-child{border:0}
.news a{display:block;font-family:"Raleway",sans-serif;font-weight:700;font-size:12px;letter-spacing:.6px;line-height:24px;color:#e8d9a0;text-transform:uppercase}
.news .date{font-size:12.5px;margin-top:6px;display:flex;gap:8px;align-items:center}
.contact-list{margin-top:22px;font-size:12.5px;line-height:22px;width:280px}
.contact-list .hq{font-weight:700}
.contact-list .row{display:flex;gap:12px;align-items:center;margin-top:14px}
.contact-list .row+.row{margin-top:4px}
.contact-list .gap{margin-top:18px}
.form{margin-top:22px;width:257px}
.form .input{height:44px;background:var(--field);color:#777;font-size:12px;padding:13px 12px;margin-bottom:20px}
.form .input.tall{height:84px}
.form .submit{width:143px;height:50px;background:var(--red);color:#fff;font-size:19px;display:flex;align-items:center;justify-content:center;margin-top:-10px}
.copyright{position:absolute;left:0;top:2966px;width:1200px;height:44px;background:var(--footer-deep);color:#ddd;font-size:12.5px;text-align:center;line-height:44px}
</style>
</head>
<body>

<div class="topbar">
  <div class="contact">
    <span><svg width="13" height="13" viewBox="0 0 24 24" fill="#ddd"><path d="M6.6 10.8a15 15 0 0 0 6.6 6.6l2.2-2.2c.3-.3.7-.4 1-.2 1.1.4 2.3.6 3.6.6.6 0 1 .4 1 1V20c0 .6-.4 1-1 1A17 17 0 0 1 3 4c0-.6.4-1 1-1h3.5c.6 0 1 .4 1 1 0 1.3.2 2.5.6 3.6.1.3 0 .7-.2 1z"/></svg>1.800.555.0142</span>
    <span><svg width="14" height="11" viewBox="0 0 24 18" fill="#ddd"><path d="M0 0h24v18H0zM2 2v1l10 7 10-7V2z"/></svg>hello@marlowevote.org</span>
  </div>
  <div class="social" aria-label="Social links"><i></i><i></i><i></i></div>
</div>

<header class="header">
  <div class="logo">MARLOWE</div>
  <nav class="nav"><a>Home</a><a>Pages</a><a>Blog</a><a>Latest News</a><a>Contact</a></nav>
  <a class="donate">Donate</a>
</header>

<section class="hero">
  <div class="hero-photo" role="img" aria-label="Waving national flag and raised hands holding up colourful VOTE letters"></div>
  <div class="reminder">Remember to vote <b>August 30, 2016!</b></div>
  <div class="hero-copy">
    <div class="kicker">VOTE FOR DEMOCRACY &amp; JUSTICE</div>
    <h1>WE NEED CHANGE</h1>
    <div class="motto">UNITY-LIBERTY-SOLIDARITY</div>
  </div>
  <div class="subscribe" style="top:177px">
    Subscribe now the latest news.<br>Together we can change the world
    <div class="field"></div>
    <div class="btn">SUBSCRIBE NOW!</div>
  </div>
</section>

<h2 class="sec-title" style="top:666px">Its Time for Change</h2>
<div class="rule" style="top:730px"></div>
<p class="lead" style="top:752px">Lorem ipsum dolor sit amet, consectetur adipiscing elit. Aenean tincidunt sit amet erat malesuada interdum. Aenean sodales dui quis leo fermentum scelerisque. Fusce condimentum dolor justo, ac tristique diam iaculis at.</p>

<div class="feature" style="left:102px">
  <div class="icon"><svg width="56" height="56" viewBox="0 0 56 56" fill="none" stroke="#fff" stroke-width="4"><circle cx="26" cy="30" r="20"/><circle cx="26" cy="30" r="11"/><circle cx="26" cy="30" r="3" fill="#fff"/><path d="M26 30 46 10M40 8v8h8"/></svg></div>
  <h3>OUR MISSION</h3><div class="line"></div>
  <p>Pellentesque habitant morbi tristique senectus et netus et malesuada fames ac turpis egestas. Vestibulum tortor quam, feugiat vitae</p>
  <a class="btn-red">Read More</a>
</div>
<div class="feature is-active" style="left:436px">
  <div class="icon"><svg width="52" height="52" viewBox="0 0 52 52" fill="#fff"><rect x="4" y="22" width="10" height="24" rx="2"/><path d="M18 24 28 6c4 0 6 3 5 7l-2 8h13c3 0 5 3 4 6l-4 16c-1 2-3 3-5 3H18z"/></svg></div>
  <h3>GET OUT AND VOTE</h3><div class="line"></div>
  <p>Pellentesque habitant morbi tristique senectus et netus et malesuada fames ac turpis egestas. Vestibulum tortor quam, feugiat vitae</p>
  <a class="btn-red">Read More</a>
</div>
<div class="feature" style="left:806px">
  <div class="icon"><svg width="60" height="40" viewBox="0 0 60 40" fill="#fff"><path d="M0 8h10v20H0zM50 8h10v20H50z"/><path d="M12 10h10l8-4 10 4h8v16l-10 8c-2 2-5 2-7 0L14 26h-2z"/><path d="M30 6l-8 10c2 2 5 2 7 0l4-4 10 10" stroke="#272a6e" stroke-width="2" fill="none"/></svg></div>
  <h3>GET INVOLVED</h3><div class="line"></div>
  <p>Pellentesque habitant morbi tristique senectus et netus et malesuada fames ac turpis egestas. Vestibulum tortor quam, feugiat vitae</p>
  <a class="btn-red">Read More</a>
</div>

<section class="about">
  <div class="label">ABOUT<br><span>MARLOWE</span></div>
  <div class="portrait" role="img" aria-label="Portrait photo of the candidate"></div>
  <h2>She has spent the last 18 years as a prosecutor fighting for victims of child abuse and sexual abuse in Alder and Brookfield counties.</h2>
  <div class="bio">
    <p>Marlowe was born and raised in Harbor City, the daughter of an air-conditioning repairman who later opened his own successful business. As the first in her family to go to college, her parents could not have been more proud as she finished her degree at Eastbrook State University, then continued on to Westlake University School of Law where she graduated with honors. Dedicating her life to public service in the central valley, she has spent the last 18 years as a prosecutor fighting for victims of child abuse and sexual abuse in Alder and Brookfield counties.</p>
    <p>She participates in local charities such as the Open Table Food Bank and the Community Reading Circle.<br>Marlowe shares her knowledge and experience freely, often mentoring the other young prosecutors and lecturing on jury selection and trial strategies. She is also committed to ensuring ethical behavior in the profession of law.</p>
  </div>
  <a class="btn-red">CONTACT US</a>
</section>

<h2 class="sec-title" style="top:1826px">Upcoming Campaign</h2>
<div class="rule" style="top:1890px"></div>
<p class="lead" style="top:1917px">Lorem ipsum dolor sit amet, consectetur adipiscing elit. Aenean tincidunt sit amet erat malesuada interdum. Aenean sodales dui quis leo fermentum scelerisque. Fusce condimentum dolor justo, ac tristique diam iaculis at.</p>

<article class="card" style="left:60px">
  <div class="photo" role="img" aria-label="Panel discussion on stage" style="background:linear-gradient(180deg,#7fb9e0,#3a4a6a 60%,#c77a3a)"></div>
  <div class="meta"><span>14 jan,2016</span><span><svg width="12" height="11" viewBox="0 0 24 22" fill="none" stroke="#d0232f" stroke-width="2.5"><path d="M12 20 3 11a5 5 0 0 1 9-7 5 5 0 0 1 9 7z"/></svg>15</span></div>
  <h4>We're the people who don't support prgres-sive change</h4>
  <p>Dramatically cultivate viral paradigms after team building e-services. Energistically network worldwide systems after highly efficient...</p>
  <a class="btn-navy">Read More</a>
</article>
<article class="card" style="left:428px">
  <div class="photo" role="img" aria-label="Group of campaign supporters on an event stage" style="background:linear-gradient(180deg,#1c2250,#3a3f7a 45%,#5a5a66)"></div>
  <div class="meta"><span>14 jan,2016</span><span><svg width="12" height="11" viewBox="0 0 24 22" fill="none" stroke="#d0232f" stroke-width="2.5"><path d="M12 20 3 11a5 5 0 0 1 9-7 5 5 0 0 1 9 7z"/></svg>15</span></div>
  <h4>We're the people who don't support prgres-sive change</h4>
  <p>Dramatically cultivate viral paradigms after team building e-services. Energistically network worldwide systems after highly efficient...</p>
  <a class="btn-navy">Read More</a>
</article>
<article class="card" style="left:799px">
  <div class="photo" role="img" aria-label="Candidate speaking with a supporter at an event" style="background:linear-gradient(135deg,#f3e6dc,#e9a17a 50%,#5a8a5a)"></div>
  <div class="meta"><span>14 jan,2016</span><span><svg width="12" height="11" viewBox="0 0 24 22" fill="none" stroke="#d0232f" stroke-width="2.5"><path d="M12 20 3 11a5 5 0 0 1 9-7 5 5 0 0 1 9 7z"/></svg>15</span></div>
  <h4>We're the people who don't support prgres-sive change</h4>
  <p>Dramatically cultivate viral paradigms after team building e-services. Energistically network worldwide systems after highly efficient...</p>
  <a class="btn-navy">Read More</a>
</article>

<footer class="footer">
  <div class="f-col" style="left:64px">
    <div class="f-head"><b>R</b>ecent News</div>
    <ul class="news">
      <li><a>3 Reasons your business needs a budget now</a><div class="date"><svg width="11" height="11" viewBox="0 0 12 12" fill="#777"><path d="M0 2h12v10H0zM1 5v6h10V5zM2 0h2v3H2zM8 0h2v3H8z"/></svg>January 26, 2016</div></li>
      <li><a>2016 Regional Small Business Week</a><div class="date"><svg width="11" height="11" viewBox="0 0 12 12" fill="#777"><path d="M0 2h12v10H0zM1 5v6h10V5zM2 0h2v3H2zM8 0h2v3H8z"/></svg>January 26, 2016</div></li>
      <li><a>The tax office doesn't always get it right</a><div class="date"><svg width="11" height="11" viewBox="0 0 12 12" fill="#777"><path d="M0 2h12v10H0zM1 5v6h10V5zM2 0h2v3H2zM8 0h2v3H8z"/></svg>January 26, 2016</div></li>
    </ul>
  </div>
  <div class="f-col" style="left:484px">
    <div class="f-head"><b>C</b>ontact Us</div>
    <div class="contact-list">
      <div class="hq">Headquarters:</div>
      <div>18 Juniper Lane Ashford Valley 20417</div>
      <div class="row gap"><svg width="11" height="11" viewBox="0 0 24 24" fill="#777"><path d="M6.6 10.8a15 15 0 0 0 6.6 6.6l2.2-2.2c.3-.3.7-.4 1-.2 1.1.4 2.3.6 3.6.6.6 0 1 .4 1 1V20c0 .6-.4 1-1 1A17 17 0 0 1 3 4c0-.6.4-1 1-1h3.5c.6 0 1 .4 1 1 0 1.3.2 2.5.6 3.6.1.3 0 .7-.2 1z"/></svg>001-555-010-2233</div>
      <div class="row"><svg width="12" height="9" viewBox="0 0 24 18" fill="#777"><path d="M0 0h24v18H0zM2 2v1l10 7 10-7V2z"/></svg>support@marlowevote.org</div>
      <div class="row gap"><svg width="11" height="11" viewBox="0 0 24 24" fill="#777"><path d="M6.6 10.8a15 15 0 0 0 6.6 6.6l2.2-2.2c.3-.3.7-.4 1-.2 1.1.4 2.3.6 3.6.6.6 0 1 .4 1 1V20c0 .6-.4 1-1 1A17 17 0 0 1 3 4c0-.6.4-1 1-1h3.5c.6 0 1 .4 1 1 0 1.3.2 2.5.6 3.6.1.3 0 .7-.2 1z"/></svg>001-555-010-4455</div>
      <div class="row"><svg width="12" height="9" viewBox="0 0 24 18" fill="#777"><path d="M0 0h24v18H0zM2 2v1l10 7 10-7V2z"/></svg>manager@marlowevote.org</div>
      <div class="row gap"><svg width="12" height="12" viewBox="0 0 24 24" fill="none" stroke="#777" stroke-width="3"><circle cx="12" cy="12" r="10"/><path d="M12 6v6l4 3"/></svg>Mon - Sat: 8:00 Am - 18:00 Pm</div>
      <div style="padding-left:24px">Sunday: Closed</div>
    </div>
  </div>
  <div class="f-col" style="left:871px">
    <div class="f-head"><b>G</b>et in Touch</div>
    <div class="form">
      <div class="input">Name</div>
      <div class="input">Email</div>
      <div class="input tall">Comment</div>
      <div class="submit">Submit</div>
    </div>
  </div>
</footer>
<div class="copyright">© 2016 MARLOWE.ORG All Right Reserved.</div>

</body>
</html>
```